Simple, High-Class Web Design Wanted - Motivational Speakers Site

1. Full Brief/Request & Specs outlined on following video -
http://clipvane-recorder.com/watch/tbWrkLmQyP

2. Use colours, images as you feel suits objective (we are happy to pay up to US$30 for any good images but must have licence/permission).

3. Layout probably similar to existing site - www.podiumvoicehub.com.au / http://podiumvoicehub.com.au/contact.php

4. Must Be Able to Coded for MOBILE-FRIENDLINESS & WordPress friendly Ideal.

5. This is the first, small job of many we/graphic design jobs. If suits, winning designer may be offered all future work direct.

Thanks & look forward to your design. Glen.

Target Market(s)

corporates - high end

Number of Pages Required

2 page

Font styles to use
Sans Serif

Requirements
Must have
• Classy professional look
Nice to have
• all in Video in brief
Should not have
• too many images / new images I haven't approved

```html
<!DOCTYPE html>
<html lang="en">
<head>
<meta charset="utf-8">
<title>Speakers — Home</title>
<link href="https://fonts.googleapis.com/css2?family=Roboto:wght@300;400;500;700&display=swap" rel="stylesheet">
<style>
:root{
  --blue:#2ba3d8;
  --ink:#3b4145;
  --muted:#7d868b;
  --line:#dde2e5;
  --panel:#f3f5f6;
  --hero:#2d363b;
  --hero-deep:#20282c;
  --side:#1e8aa3;
  --footer:#238ba6;
  --footer-deep:#1b7189;
  --white:#ffffff;
}
*{box-sizing:border-box;margin:0;padding:0}
html,body{width:851px;height:1200px;overflow:hidden}
body{
  font-family:"Roboto",Arial,sans-serif;color:var(--ink);
  background:linear-gradient(180deg,var(--hero-deep) 0,var(--hero-deep) 420px,var(--side) 560px,#2aa1bb 1100px,var(--footer-deep) 1200px);
  position:relative;
}
a{text-decoration:none}
.page{position:absolute;left:62px;top:0;width:727px;height:1200px}

/* header */
.site-header{position:absolute;left:0;top:0;width:727px;height:64px;background:var(--hero-deep)}
.brand{position:absolute;left:-30px;top:2px;font-weight:300;font-size:50px;color:var(--white);letter-spacing:.5px}
.main-nav{position:absolute;right:-10px;top:30px;display:flex;gap:36px;font-size:14px}
.main-nav a{color:var(--white)}
.main-nav a.active{color:var(--blue)}

/* hero */
.hero{position:absolute;left:0;top:64px;width:727px;height:352px;
  background:radial-gradient(ellipse at 50% 40%,#3c474d 0,var(--hero) 55%,var(--hero-deep) 100%)}
.video-frame{position:absolute;left:123px;top:8px;width:480px;height:226px;
  background:linear-gradient(180deg,#d9dde0 0,#bfc6cb 55%,#8b959c 100%);border:3px solid #50595e}
.play{position:absolute;left:220px;top:93px;width:40px;height:40px}
.hero-title{position:absolute;left:0;top:248px;width:727px;text-align:center;color:var(--white);font-size:25px;font-weight:400}
.btn{display:inline-block;background:var(--blue);color:var(--white);font-size:11px;font-weight:500;text-align:center;border-radius:2px}
.hero .btn{position:absolute;left:302px;top:292px;width:124px;height:25px;line-height:25px}

/* feature tabs */
.features{position:absolute;left:0;top:420px;width:727px;height:128px;display:flex;justify-content:space-between;padding:0 14px}
.feature{width:222px;height:118px;background:var(--white);border-radius:3px;position:relative;box-shadow:0 2px 4px rgba(0,0,0,.18)}
.feature h3{height:30px;line-height:30px;background:var(--panel);font-size:12px;font-weight:500;padding-left:12px;color:var(--ink);border-bottom:1px solid var(--line)}
.feature .icon{position:absolute;left:10px;top:44px;width:42px;height:42px;border-radius:50%;background:var(--blue)}
.feature p{position:absolute;left:62px;top:42px;right:12px;font-size:8.5px;line-height:12px;color:var(--muted)}

/* content area */
.content{position:absolute;left:0;top:548px;width:727px;height:540px;background:var(--white)}
.welcome-photo{position:absolute;left:42px;top:20px;width:278px;height:192px;background:linear-gradient(135deg,#c9b5a6 0,#9c7f6f 55%,#5a4a44 100%)}
.welcome h2{position:absolute;left:358px;top:24px;font-size:22px;font-weight:400;color:var(--blue)}
.welcome p{position:absolute;left:358px;top:62px;width:320px;font-size:9px;line-height:13px;color:var(--muted)}
.welcome .btn{position:absolute;left:358px;top:152px;width:114px;height:26px;line-height:26px}
.divider{position:absolute;left:28px;top:244px;width:670px;height:1px;background:var(--line)}

.col{position:absolute;top:262px;width:210px}
.col h3{font-size:17px;font-weight:400;color:var(--blue);display:flex;align-items:center;gap:8px;height:26px;white-space:nowrap}
.col h3 svg{flex:none}
.col-resources{left:26px;width:200px}
.col-resources p{font-size:9px;line-height:12.5px;color:var(--muted);margin-top:14px}
.col-events{left:254px}
.event{display:flex;gap:10px;margin-top:12px;height:54px;border-bottom:1px solid var(--line)}
.event:first-of-type{margin-top:16px}
.date{width:40px;height:46px;background:var(--blue);color:var(--white);text-align:center;padding-top:4px;flex:none}
.date b{display:block;font-size:20px;font-weight:500;line-height:22px}
.date span{font-size:9px}
.event-text{flex:1;font-size:9px;line-height:12px;color:var(--muted);position:relative}
.event-text a{position:absolute;right:0;bottom:8px;font-size:8px;color:var(--ink);font-weight:500}
.col-contact{left:484px;width:216px}
.field{margin-top:8px;height:20px;border:1px solid var(--line);font-size:8.5px;color:#a6aeb2;padding:5px 8px}
.field:first-of-type{margin-top:16px}
.field.message{height:62px}
.col-contact .btn{display:block;margin:10px 0 0 auto;width:106px;height:26px;line-height:26px}

/* footer */
.site-footer{position:absolute;left:0;top:1088px;width:727px;height:80px;background:var(--footer);color:var(--white)}
.footer-item{position:absolute;top:22px;display:flex;align-items:center;gap:10px;font-size:8.5px;line-height:12px}
.footer-item .ring{width:26px;height:26px;border-radius:50%;border:1.5px solid var(--white);display:flex;align-items:center;justify-content:center;flex:none}
.fi-address{left:22px}.fi-phone{left:292px}.fi-mail{left:484px}
.copyright{position:absolute;left:0;top:1172px;width:727px;height:22px;font-size:8px;color:var(--white);padding-left:26px;line-height:22px}
.social{position:absolute;right:22px;top:5px;display:flex;gap:6px}
.social i{display:block;width:12px;height:12px;border-radius:50%;background:var(--white);opacity:.85}
</style>
</head>
<body>
<div class="page">

  <header class="site-header">
    <div class="brand">Speakers</div>
    <nav class="main-nav">
      <a class="active" href="#">Home</a>
      <a href="#">Speakers</a>
      <a href="#">Entertainers</a>
      <a href="#">About Us</a>
      <a href="#">Contact Us</a>
    </nav>
  </header>

  <section class="hero">
    <div class="video-frame" role="img" aria-label="Video still of a speaker presenting to camera">
      <svg class="play" viewBox="0 0 40 40"><circle cx="20" cy="20" r="19" fill="rgba(255,255,255,.85)"/><path d="M16 12 L28 20 L16 28 Z" fill="#2d363b"/></svg>
    </div>
    <h1 class="hero-title">I Want to Make our Event a Great Success</h1>
    <a class="btn" href="#">View More Video</a>
  </section>

  <section class="features">
    <div class="feature">
      <h3>Information</h3>
      <div class="icon"></div>
      <p>Any information you provide will help us match the right speaker to your event needs.</p>
    </div>
    <div class="feature">
      <h3>Agreements</h3>
      <div class="icon"></div>
      <p>Work with us on clear financial agreements with each individual speaker we recommend.</p>
    </div>
    <div class="feature">
      <h3>Understand</h3>
      <div class="icon"></div>
      <p>Please understand that while fees vary, we respond quickly to every speaking brief.</p>
    </div>
  </section>

  <main class="content">
    <div class="welcome-photo" role="img" aria-label="Photo of an audience taking notes at a seminar"></div>
    <div class="welcome">
      <h2>Welcome to The Spekers</h2>
      <p>Lorem Ipsum is simply dummy text of the printing and typesetting industry. Lorem Ipsum has been the industry's standard dummy text ever since the 1500s, when an unknown printer took a galley of type and scrambled it to make a type specimen book. It has survived not only five centuries, but also the leap into electronic typesetting.</p>
      <a class="btn" href="#">READ MORE</a>
    </div>
    <div class="divider"></div>

    <section class="col col-resources">
      <h3><svg width="18" height="18" viewBox="0 0 20 20"><path d="M10 2v16M2 10h16M4.5 4.5l11 11M15.5 4.5l-11 11" stroke="#2ba3d8" stroke-width="2"/></svg>Helpful Resources</h3>
      <p>Topic/Style – Motivation, Entertaining, Keynote/Workshop, MC etc</p>
      <p>Topic / Area – Team Building, Leadership, Inspiration, Health, Life Balance etc</p>
      <p>Approximate Budget – $1000, $2000, $3000, $7000+ etc</p>
      <p>Location – Sydney, Melbourne, Brisbane, Perth, Adelaide, Canberra etc</p>
    </section>

    <section class="col col-events">
      <h3><svg width="18" height="18" viewBox="0 0 20 20"><rect x="2" y="4" width="16" height="14" fill="none" stroke="#2ba3d8" stroke-width="2"/><path d="M2 8h16M6 2v4M14 2v4" stroke="#2ba3d8" stroke-width="2"/></svg>Seminars and Events</h3>
      <div class="event"><div class="date"><b>3</b><span>Nov</span></div><div class="event-text">Lorem Ipsum has been the industry's standard...<a href="#">READ MORE</a></div></div>
      <div class="event"><div class="date"><b>3</b><span>Nov</span></div><div class="event-text">Lorem Ipsum has been the industry's standard...<a href="#">READ MORE</a></div></div>
      <div class="event"><div class="date"><b>3</b><span>Nov</span></div><div class="event-text">Lorem Ipsum has been the industry's standard...<a href="#">READ MORE</a></div></div>
    </section>

    <section class="col col-contact">
      <h3><svg width="18" height="18" viewBox="0 0 20 20"><path d="M3 17l2-5 9-9 3 3-9 9z" fill="none" stroke="#2ba3d8" stroke-width="2"/></svg>Quick Contact Form</h3>
      <div class="field">Name</div>
      <div class="field">Email</div>
      <div class="field">Phone</div>
      <div class="field message">Message</div>
      <a class="btn" href="#">SEND MAIL</a>
    </section>
  </main>

  <footer class="site-footer">
    <div class="footer-item fi-address">
      <span class="ring"><svg width="12" height="14" viewBox="0 0 12 14"><path d="M6 13S1 7.5 1 5a5 5 0 0 1 10 0c0 2.5-5 8-5 8z" fill="#fff"/><circle cx="6" cy="5" r="1.8" fill="#238ba6"/></svg></span>
      <span>LECTERN CIRCLE<br>PO Box 702 Kestrel Bay NSW 2119</span>
    </div>
    <div class="footer-item fi-phone">
      <span class="ring"><svg width="12" height="12" viewBox="0 0 12 12"><path d="M2 1l2.5 0 1 3-1.5 1a7 7 0 0 0 3 3l1-1.5 3 1V10a1 1 0 0 1-1 1A10 10 0 0 1 1 2a1 1 0 0 1 1-1z" fill="#fff"/></svg></span>
      <span>1300 640 271</span>
    </div>
    <div class="footer-item fi-mail">
      <span class="ring"><svg width="13" height="10" viewBox="0 0 13 10"><rect x="0.5" y="0.5" width="12" height="9" fill="#fff"/><path d="M1 1l5.5 4.5L12 1" fill="none" stroke="#238ba6"/></svg></span>
      <span>hello@lecterncircle.net</span>
    </div>
  </footer>
  <div class="copyright">© www.podiumvoicehub.com.au – All Rights Reserved
    <div class="social"><i></i><i></i><i></i></div>
  </div>

</div>
</body>
</html>
```